ebook cover: book 4 in the We Hum Lantern series. Lantern by Riverside

I am wanting a striking cover to bring the forth book in a spiritual journey series to an audience ready to meet new characters and get excited again! White backgrounds, red titles (any font), subtitles to introduce a new major character in the series of ten (same fonts please as the original, We Hum Lantern), and one emblematic, slightly mysterious image. Please keep to the same colour tones as the original, but the lead image need not be gray. Let's please try to use the "light flash" that is on the tin can in We Hum Lantern somehow, in your own way. It is meant to signify the other side, or the higher light, or some such inference.

Book details:
Title: Lantern by Riverside
Subtitle: Archangel Veloriel brings the message
Image: silver hourglass
Author: Maren Tulliver, Ph.D
Strap quote: "Tulliver is smart, savvy and full of ideas," Harbourgate Ledger

Please do your best: this one is going in competition of spiritual healers!

Thanks! :)

```html
<!DOCTYPE html>
<html lang="en">
<head>
<meta charset="utf-8">
<title>Lantern by Riverside — ebook cover</title>
<link href="https://fonts.googleapis.com/css2?family=Mrs+Saint+Delafield&family=Open+Sans:wght@300;400;600&display=swap" rel="stylesheet">
<style>
  :root {
    --stage: #ecebed;
    --paper: #ffffff;
    --title-red: #a3191f;
    --ink: #1e1e1e;
    --author-grey: #555555;
    --glass-light: #f6f6f6;
    --glass-mid: #d9d9d9;
    --glass-shadow: #bdbdbd;
  }
  * { box-sizing: border-box; margin: 0; padding: 0; }
  html, body {
    width: 1200px;
    height: 800px;
    overflow: hidden;
    background: var(--stage);
  }
  .stage {
    width: 1200px;
    height: 800px;
    display: flex;
    align-items: center;
    justify-content: center;
  }
  .cover {
    position: relative;
    width: 520px;
    height: 766px;
    background: var(--paper);
    box-shadow: 0 6px 18px rgba(0,0,0,0.18);
    font-family: "Open Sans", sans-serif;
    overflow: hidden;
  }
  .strap-quote {
    position: absolute;
    top: 30px;
    left: 0;
    width: 100%;
    text-align: center;
    font-size: 9.5px;
    line-height: 1.5;
    font-weight: 600;
    color: var(--ink);
    text-transform: uppercase;
  }
  .strap-quote .source { display: block; font-size: 11.5px; font-weight: 400; }
  .title {
    position: absolute;
    top: 84px;
    left: 30px;
    width: 460px;
    text-align: center;
    font-family: "Mrs Saint Delafield", cursive;
    font-weight: 400;
    font-size: 64px;
    line-height: 1.3;
    color: var(--title-red);
    white-space: nowrap;
  }
  .subtitle {
    position: absolute;
    top: 196px;
    left: 0;
    width: 100%;
    text-align: center;
    font-size: 25px;
    line-height: 1.22;
    font-weight: 600;
    letter-spacing: 0.2em;
    text-transform: uppercase;
    color: var(--ink);
    padding-left: 0.2em;
  }
  .lead-image {
    position: absolute;
    top: 278px;
    left: 160px;
    width: 200px;
    height: 400px;
    border-radius: 30px 30px 20px 20px;
    background:
      radial-gradient(ellipse at 50% 30%, var(--glass-light) 0%, var(--glass-mid) 60%, var(--glass-shadow) 100%);
  }
  .author {
    position: absolute;
    top: 696px;
    left: 0;
    width: 100%;
    text-align: center;
    font-size: 29px;
    font-weight: 300;
    letter-spacing: 0.04em;
    color: var(--author-grey);
    text-transform: uppercase;
  }
  .author .credential { font-variant: small-caps; text-transform: none; }
</style>
</head>
<body>
  <main class="stage">
    <article class="cover">
      <p class="strap-quote">Tulliver is smart, savvy and full of ideas,
        <span class="source">- Harbourgate Ledger</span></p>
      <h1 class="title">Lantern by Riverside</h1>
      <h2 class="subtitle">Archangel Veloriel<br>brings the message</h2>
      <div class="lead-image" role="img" aria-label="Photograph of a silver hourglass with white sand, lit by a soft flash of light"></div>
      <p class="author">Maren Tulliver <span class="credential">Ph.D.</span></p>
    </article>
  </main>
</body>
</html>
```